Unique Business Card Design

Unique Business Card design for our orthotic and prosthetic company. Our logo is on our website, color is light blue. Unique shape (artificial leg shaped, vertical, etc..) preferred. Logo, business name, individual name and basic demographics needed.

Industry/Entity Type

Business

Contact Information for Business Card

Logo, Industry, Phone # Logo, "Prosthetic & Orthotic Services" Place to add individual name and contact info

Colors
cee9f5

Requirements
Must have
• The icon must be there, placement of "Prosthetic & Orthotic Services" can be moved
Nice to have
• Like the mix of light blue, and a little darker blue. One design included the icons from my website which was a nice touch

```html
<!DOCTYPE html>
<html lang="en">
<head>
<meta charset="utf-8">
<title>Limbwell Inc. Business Card</title>
<link rel="stylesheet" href="https://fonts.googleapis.com/css2?family=Roboto:wght@400;500;700&family=Crimson+Text:ital@1&display=swap">
<style>
  :root {
    --backdrop: #8a8a8a;
    --card-dark: #2b2b2b;
    --card-light: #ffffff;
    --sky: #cee9f5;
    --brand-blue: #1f5bab;
    --text-grey: #555555;
    --faint: #f1f6fa;
  }
  * { margin: 0; padding: 0; box-sizing: border-box; }
  html, body { width: 1200px; height: 1000px; overflow: hidden; }
  body { background: var(--backdrop); position: relative; font-family: "Roboto", Arial, sans-serif; }

  .card { position: absolute; left: 220px; width: 760px; border-radius: 28px; overflow: hidden; }
  .card-front { top: 52px; height: 432px; background: var(--card-dark); }
  .card-back { top: 524px; height: 436px; background: var(--card-light); }

  .brand-mark { position: absolute; border-radius: 50%; }
  .brand-name { position: absolute; font-family: "Roboto", Arial, sans-serif; font-weight: 500; white-space: nowrap; letter-spacing: 0.5px; }
  .brand-rule { position: absolute; height: 4px; }
  .brand-tagline { position: absolute; font-family: "Crimson Text", Georgia, serif; font-style: italic; white-space: nowrap; }

  .card-front .brand-mark { left: 121px; top: 145px; width: 140px; height: 140px; background: var(--sky); }
  .card-front .brand-name { left: 278px; top: 164px; font-size: 40px; color: var(--sky); }
  .card-front .brand-rule { left: 285px; top: 214px; width: 350px; background: var(--sky); }
  .card-front .brand-tagline { left: 300px; top: 226px; font-size: 23px; color: var(--sky); }
  .front-url { position: absolute; left: 0; right: 0; top: 372px; text-align: center; color: #ffffff; font-size: 16px; letter-spacing: 0.3px; }

  .back-watermark { position: absolute; left: 362px; top: 128px; width: 400px; height: 400px; border-radius: 50%; background: var(--faint); }
  .back-tab { position: absolute; left: 0; top: 43px; width: 10px; height: 37px; background: var(--brand-blue); border-radius: 0 4px 4px 0; }
  .holder-name { position: absolute; left: 42px; top: 40px; font-size: 21px; font-weight: 700; color: var(--brand-blue); }
  .holder-title { position: absolute; left: 42px; top: 68px; font-size: 16px; color: var(--text-grey); }

  .card-back .brand-mark { left: 362px; top: 40px; width: 98px; height: 98px; background: var(--brand-blue); }
  .card-back .brand-name { left: 470px; top: 57px; font-size: 27px; color: var(--brand-blue); }
  .card-back .brand-rule { left: 473px; top: 91px; width: 240px; height: 3px; background: var(--brand-blue); }
  .card-back .brand-tagline { left: 486px; top: 96px; font-size: 16px; color: var(--brand-blue); }

  .address { position: absolute; left: 42px; top: 190px; font-size: 16.5px; line-height: 22px; color: var(--text-grey); font-style: normal; }
  .address .company { color: var(--brand-blue); }
  .contact-list { position: absolute; left: 42px; top: 275px; list-style: none; font-size: 16.5px; color: var(--text-grey); }
  .contact-list li { height: 24.5px; display: flex; align-items: center; gap: 6px; }
  .contact-list svg { width: 14px; height: 14px; fill: var(--brand-blue); flex: none; }
  .contact-list .url-core { color: var(--brand-blue); }
</style>
</head>
<body>
  <section class="card card-front">
    <div class="brand-mark"></div>
    <div class="brand-name">LIMBWELL INC.</div>
    <div class="brand-rule"></div>
    <div class="brand-tagline">Prosthetic &amp; Orthotic Services</div>
    <div class="front-url">www.limbwellinc.com</div>
  </section>

  <section class="card card-back">
    <div class="back-watermark"></div>
    <div class="back-tab"></div>
    <div class="holder-name">Mira Hollander</div>
    <div class="holder-title">CO LPO</div>

    <div class="brand-mark"></div>
    <div class="brand-name">LIMBWELL INC.</div>
    <div class="brand-rule"></div>
    <div class="brand-tagline">Prosthetic &amp; Orthotic Services</div>

    <address class="address">
      <div class="company">LIMBWELL INC.</div>
      <div>820 Harbor Lane</div>
      <div>Brooklyn, NY 11230</div>
    </address>

    <ul class="contact-list">
      <li><svg viewBox="0 0 14 14"><path d="M4 0h6a1 1 0 0 1 1 1v12a1 1 0 0 1-1 1H4a1 1 0 0 1-1-1V1a1 1 0 0 1 1-1zm0.5 1.5v9.5h5V1.5zM7 11.6a0.8 0.8 0 1 0 0 1.6 0.8 0.8 0 0 0 0-1.6z"/></svg>845-5550142</li>
      <li><svg viewBox="0 0 14 14"><path d="M3 1l2.2 2.6-1.2 1.6c0.9 2 2.5 3.6 4.6 4.6l1.6-1.2L13 11l-1.4 2C6.4 12.6 1.4 7.6 1 2.4z"/></svg>(718) 555-0180</li>
      <li><svg viewBox="0 0 14 14"><path d="M3.5 1h7v3h-7zM1 5h12v6h-2.5V9h-7v2H1zM4.5 10h5v3h-5z"/></svg>(718) 555-0193</li>
      <li><svg viewBox="0 0 14 14"><path d="M1 3h12v1L7 8 1 4zM1 5.5l6 4 6-4V11H1z"/></svg>Mhollander@limbwellinc.com</li>
      <li><svg viewBox="0 0 14 14"><path d="M7 1a6 6 0 1 0 0 12A6 6 0 0 0 7 1zm0 1.3c0.7 0.8 1.2 2 1.4 3.2H5.6C5.8 4.3 6.3 3.1 7 2.3zM2.4 6.5h2c0 0.4 0 0.7 0 1h-2a4.7 4.7 0 0 1 0-1zm3.2 2h2.8C8.2 9.7 7.7 10.9 7 11.7 6.3 10.9 5.8 9.7 5.6 8.5zm4 0h2a4.7 4.7 0 0 1-2.2 2.9c0.1-0.9 0.2-1.9 0.2-2.9zm0-2h2a4.7 4.7 0 0 1 0 1h-2zM5.6 7.5c0-0.3 0-0.7 0-1h2.8v1z"/></svg>www.<span class="url-core">limbwellinc</span>.net</li>
    </ul>
  </section>
</body>
</html>
```